Business Card Project for Firm Deck Hoisting

Business name is "Firm Deck Hoisting" we are a scaffolding & rigging business specialising in local and remote work for:
- scaffolding (residential, commercial, industrial)
- rigging
-man material hoists
- swing stages
- labour hire

On the back of the card I would like FDH as the symbol / logo. I have attached the logos we have had created by sketch harbour. We would like to use bold colours – preferably as the same colour scheme as the logo.

Target Market(s)

Construction business

Industry/Entity Type

Construction

Contact Information for Business Card

name: Owen Pellew
Title: Director
Phone: 0491 572 864
Address: PO BOX 3251, Kelsworth SA 5199
Email: owen@firmdeckhoisting.com.au
Website: www.firmdeckhoisting.com.au

Font styles to use
Sans Serif

Requirements
Must have
• Must use existing logo & prefering using bold colours
Nice to have
• Would be nice to have a line of dot points in what we specialise in but not essential
• Would be nice to see some designs with a slogan but not essential
Should not have
• NA

```html
<!DOCTYPE html>
<html lang="en">
<head>
<meta charset="utf-8">
<title>Firm Deck Hoisting – Business Card</title>
<link href="https://fonts.googleapis.com/css2?family=Roboto:wght@400;500;700;900&display=swap" rel="stylesheet">
<style>
  :root {
    --backdrop: #3b302c;
    --card: #141414;
    --white: #ffffff;
    --blue: #2f7fd0;
    --soft: #e6e6e6;
  }
  * { box-sizing: border-box; margin: 0; padding: 0; }
  html, body { width: 1200px; height: 900px; overflow: hidden; }
  body {
    background: var(--backdrop);
    font-family: "Roboto", Arial, sans-serif;
    position: relative;
  }
  .card {
    position: absolute;
    top: 295px;
    width: 540px;
    height: 310px;
    background: var(--card);
    border-radius: 4px;
    box-shadow: 0 10px 30px rgba(0,0,0,0.45);
    color: var(--white);
  }
  .card--front { left: 40px; }
  .card--back { left: 620px; }

  /* front */
  .front-mark {
    position: absolute;
    left: 46px;
    top: 40px;
    font-weight: 900;
    font-size: 104px;
    line-height: 1;
    letter-spacing: 4px;
    color: var(--white);
  }
  .person {
    position: absolute;
    left: 46px;
    top: 196px;
    width: 150px;
  }
  .person__name {
    font-weight: 500;
    font-size: 17px;
    letter-spacing: 0.5px;
    white-space: nowrap;
  }
  .person__title {
    margin-top: 3px;
    font-size: 15px;
    color: var(--blue);
    text-align: right;
    padding-right: 4px;
  }
  .contacts {
    position: absolute;
    left: 210px;
    top: 168px;
    list-style: none;
  }
  .contacts li {
    display: flex;
    align-items: center;
    gap: 8px;
    font-size: 15px;
    line-height: 23px;
    color: var(--soft);
    white-space: nowrap;
  }
  .contacts svg { width: 13px; height: 13px; flex: none; }
  .website {
    position: absolute;
    left: 0;
    right: 0;
    bottom: 26px;
    text-align: center;
    font-size: 15px;
    color: var(--soft);
    letter-spacing: 0.3px;
  }

  /* back */
  .back-lockup {
    position: absolute;
    left: 0;
    right: 0;
    top: 92px;
    display: flex;
    justify-content: center;
    align-items: center;
    gap: 14px;
    color: var(--white);
    font-weight: 700;
  }
  .back-lockup__mark { font-size: 52px; letter-spacing: 2px; }
  .back-lockup__rule { width: 2px; height: 52px; background: var(--blue); }
  .back-lockup__name { font-size: 22px; line-height: 1.15; letter-spacing: 1.5px; }
  .services {
    position: absolute;
    left: 0;
    right: 0;
    top: 212px;
    text-align: center;
    font-size: 11.5px;
    font-weight: 500;
    letter-spacing: 0.6px;
    line-height: 20px;
    color: var(--soft);
  }
  .services .dot {
    display: inline-block;
    width: 6px;
    height: 6px;
    border-radius: 50%;
    background: var(--blue);
    margin: 0 7px;
    vertical-align: middle;
  }
</style>
</head>
<body>

<section class="card card--front" aria-label="Business card front">
  <div class="front-mark">FDH</div>

  <div class="person">
    <div class="person__name">OWEN PELLEW</div>
    <div class="person__title">DIRECTOR</div>
  </div>

  <ul class="contacts">
    <li>
      <svg viewBox="0 0 13 13" aria-hidden="true"><rect width="13" height="13" rx="2" fill="#2f7fd0"/><path d="M6.5 2.5a2.6 2.6 0 0 0-2.6 2.6c0 2 2.6 5.2 2.6 5.2s2.6-3.2 2.6-5.2a2.6 2.6 0 0 0-2.6-2.6zm0 3.6a1 1 0 1 1 0-2 1 1 0 0 1 0 2z" fill="#fff"/></svg>
      PO BOX 3251, Kelsworth SA 5199
    </li>
    <li>
      <svg viewBox="0 0 13 13" aria-hidden="true"><rect width="13" height="13" rx="2" fill="#2f7fd0"/><path d="M4 2.8l1.3 1.9-.8.9c.5 1.2 1.4 2.1 2.6 2.6l.9-.8 1.9 1.3-.6 1.4C6.6 10 3 6.4 2.9 3.4z" fill="#fff"/></svg>
      0491 572 864
    </li>
    <li>
      <svg viewBox="0 0 13 13" aria-hidden="true"><rect width="13" height="13" rx="2" fill="#2f7fd0"/><rect x="2.5" y="3.8" width="8" height="5.6" fill="#fff"/><path d="M2.5 3.8l4 3 4-3" fill="none" stroke="#2f7fd0" stroke-width="0.9"/></svg>
      owen@firmdeckhoisting.com.au
    </li>
  </ul>

  <div class="website">www.firmdeckhoisting.com.au</div>
</section>

<section class="card card--back" aria-label="Business card back">
  <div class="back-lockup">
    <span class="back-lockup__mark">FDH</span>
    <span class="back-lockup__rule"></span>
    <span class="back-lockup__name">FIRM DECK<br>HOISTING</span>
  </div>

  <div class="services">
    SCAFFOLDING (RESIDENTIAL, COMMERCIAL, INDUSTRIAL)<br>
    RIGGING<span class="dot"></span>MAN MATERIAL HOISTS<span class="dot"></span>SWING STAGES<span class="dot"></span>LABOUR HIRE
  </div>
</section>

</body>
</html>
```